Cybersecurity Start-Up - Velorix

We need a MS Word Template for everyday documents. This would be leveraged to create reports, marketing materials, internal memos etc.

The document should follow the standard MS Word template format and have an H1,H2,H3, paragraph, Title, bold font, regular font, table etc. All editable with normal MS Word features.

Our logo is also attached. We would like to see the same color scheme used throughout the document. Additional attached is a sample word document that outlines all of the components we would like to see in the template.

Requirements
Must have
• - Submission must meet all standard MS Word Template requirements.
• - Submission should make use of Built in MS Styles so as the user of the template I should be able to create a brand new page and insert an H1 for example and be able to select from the styles drop down the same font/color/style that you have designed for your submission.
• - All sections in the provided document need to be contained in your submission.
• - The table of contents should auto update if I add a new page, heading, section etc.
• - Need to read and understand all of my comments which I have placed in the sample document uploaded to the briefing
Should not have
• no fixed textboxes or image boxes. everything needs to be smoothly editable in MS Word. "Editable" means more than just being able to alter text.

```html
<!DOCTYPE html>
<html lang="en">
<head>
<meta charset="utf-8">
<title>Velorix – Document Template Pages</title>
<link rel="stylesheet" href="https://fonts.googleapis.com/css2?family=Nunito+Sans:wght@400;600;700&display=swap">
<style>
  :root{
    --orange:#f26b3a;
    --ink:#2d2f36;
    --grey:#6d6f75;
    --rule:#d9d9d9;
    --bar:#3a3a3a;
    --dark-a:#1c1c1c;
    --dark-b:#3b3b3b;
    --navy-a:#0e1d42;
    --navy-b:#1e3a7c;
    --red:#e0241b;
    --amber:#f39a1e;
    --blue:#1a8fd6;
    --green:#7cc242;
    --paper:#ffffff;
  }
  *{box-sizing:border-box;margin:0;padding:0}
  html,body{width:1200px;height:1200px;overflow:hidden;background:var(--paper)}
  body{font-family:"Nunito Sans",sans-serif;color:var(--ink)}
  .sheet{position:relative;width:1200px;height:1200px;padding-top:6px}
  .row{display:flex;justify-content:center;gap:5px;margin-bottom:8px}
  .page{position:relative;width:205px;height:289px;background:var(--paper);overflow:hidden;box-shadow:0 0 2px rgba(0,0,0,.35)}

  /* covers */
  .cover-light{background:linear-gradient(135deg,#ececec 0%,#fafafa 35%,#fff 60%)}
  .cover-dark{background:linear-gradient(135deg,var(--dark-a),var(--dark-b) 40%,#2a2a2a)}
  .cover-navy{background:linear-gradient(135deg,var(--navy-a),var(--navy-b) 45%,#14295a)}
  .brand{position:absolute;left:68px;top:116px;display:flex;align-items:center;gap:4px}
  .brand-name{font-size:25px;font-weight:600;letter-spacing:.2px;color:var(--ink)}
  .brand-dot{width:26px;height:26px;border-radius:50%;border:3px solid var(--orange)}
  .cover-dark .brand-name,.cover-navy .brand-name{color:#fff}
  .cover-title{position:absolute;right:30px;top:160px;font-size:11px;font-weight:600;color:var(--orange)}
  .cover-date{position:absolute;left:25px;bottom:6px;font-size:3.6px;color:var(--grey)}
  .cover-dark .cover-date,.cover-navy .cover-date{color:#bbb}
  .back .brand{left:auto;right:20px;top:112px}
  .contact{position:absolute;right:24px;top:155px;text-align:right;font-size:4.2px;line-height:7px;color:var(--ink)}
  .contact .who{font-size:6.4px;font-weight:600;color:var(--orange);margin-bottom:2px}
  .cover-dark .contact,.cover-navy .contact{color:#fff}

  /* interior */
  .pg-head{position:absolute;left:18px;top:13px;display:flex;align-items:center}
  .pg-head-mark{width:26px;height:26px;border-radius:50%;border:1.5px solid rgba(242,107,58,.55)}
  .pg-head h1{position:absolute;left:6px;top:7px;white-space:nowrap;font-size:9.5px;font-weight:600;color:var(--ink)}
  .content{position:absolute;left:24px;right:24px;top:60px}
  .footer{position:absolute;left:0;right:0;bottom:0;height:8px;background:var(--bar)}
  .footer::after{content:"";position:absolute;left:50%;top:1px;width:6px;height:6px;margin-left:-3px;border-radius:50%;background:var(--orange)}
  p.body{font-size:2.5px;line-height:3.4px;color:var(--grey);margin-bottom:4px}
  h2.sub{font-size:4.2px;font-weight:700;color:var(--orange);margin:5px 0 2px}
  h3.minor{font-size:3.2px;font-weight:700;color:var(--ink);margin:3px 0 1px}

  /* contents */
  .toc{position:absolute;left:24px;right:18px;top:70px;list-style:none}
  .toc li{display:flex;justify-content:space-between;font-size:3.8px;line-height:8.8px;color:var(--grey)}
  .toc .l2{padding-left:7px}
  .toc .l3{padding-left:14px}

  /* tables */
  table{width:100%;border-collapse:collapse;font-size:2.5px;color:var(--grey)}
  td,th{padding:.6px 1.5px;text-align:left;font-weight:400;border-bottom:.3px solid var(--rule)}
  .tbl-rule{border-top:.6px solid var(--orange);border-bottom:.6px solid var(--orange);margin-bottom:6px}
  .tbl-rule th{font-weight:700;color:var(--ink);border-bottom:.6px solid var(--orange)}
  .tbl-orange thead tr:first-child th{background:var(--orange);color:#fff;font-weight:700}
  .tbl-orange thead tr:nth-child(2) th{background:#f7a37f;color:var(--ink);font-weight:700}
  .tbl-orange{border:.4px solid var(--orange);margin-bottom:3px}
  .dot{display:inline-block;width:3px;height:3px;border-radius:50%;vertical-align:middle;margin-right:3px}
  .c{background:var(--red)}.h{background:var(--amber)}.m{background:var(--blue)}.lw{background:var(--green)}
  .t-c{color:var(--red)}.t-h{color:var(--amber)}.t-m{color:var(--blue)}.t-l{color:var(--green)}

  /* finding card */
  .finding{border:.5px solid #555;margin:3px 0 6px}
  .finding-head{display:flex;justify-content:space-between;align-items:center;background:var(--bar);color:#fff;font-size:2.6px;font-weight:700;line-height:3px;padding:1.2px 2px}
  .sev{width:7px;height:7px;border-radius:50%;border:.5px solid #fff}
  .finding-row{display:flex;border-top:.3px solid var(--rule)}
  .finding-label{width:50px;padding:2px;font-size:2.6px;color:var(--ink);display:flex;align-items:center}
  .finding-body{flex:1;padding:2px;font-size:2.5px;line-height:3.3px;color:var(--grey)}
  .finding-body ul{padding-left:4px}
  .evidence{width:44px;height:66px;border:.4px solid var(--rule);background:linear-gradient(180deg,#fff 0%,#fff 25%,#f7b08f 30%,#f2f2f2 34%,#e2e2e2 60%,#cfcfcf 100%);border-bottom:1.5px solid var(--bar)}
</style>
</head>
<body>
<main class="sheet">

  <!-- row 1: covers + contents -->
  <section class="row">
    <article class="page cover-light" role="img" aria-label="Cover, light version">
      <div class="brand"><span class="brand-name">Velorix</span><span class="brand-dot"></span></div>
      <div class="cover-title">Training Name</div>
      <div class="cover-date">DD/MM/YYY</div>
    </article>
    <article class="page cover-dark">
      <div class="brand"><span class="brand-name">Velorix</span><span class="brand-dot"></span></div>
      <div class="cover-title">Training Name</div>
      <div class="cover-date">DD/MM/YYY</div>
    </article>
    <article class="page cover-navy">
      <div class="brand"><span class="brand-name">Velorix</span><span class="brand-dot"></span></div>
      <div class="cover-title">Training Name</div>
      <div class="cover-date">DD/MM/YYY</div>
    </article>
    <article class="page">
      <header class="pg-head"><span class="pg-head-mark"></span><h1>Table of contents</h1></header>
      <ul class="toc">
        <li><span>Table of contents</span><span>04</span></li>
        <li><span>Subject introduction</span><span>05</span></li>
        <li class="l2"><span>Subjects recommended</span><span>05</span></li>
        <li class="l2"><span>Professional outcomes</span><span>05</span></li>
        <li><span>Training content</span><span>06</span></li>
        <li><span>Technical overview</span><span>07</span></li>
        <li class="l2"><span>Severity ratings</span><span>07</span></li>
        <li class="l2"><span>Summary of findings</span><span>08</span></li>
        <li class="l2"><span>Detailed observations</span><span>08</span></li>
        <li class="l3"><span>Critical findings</span><span>08</span></li>
        <li class="l3"><span>High findings</span><span>09</span></li>
        <li class="l3"><span>Medium findings</span><span>10</span></li>
        <li class="l3"><span>Low findings</span><span>11</span></li>
        <li><span>Appendix 01</span><span>12</span></li>
        <li class="l2"><span>Engagement methodology</span><span>12</span></li>
      </ul>
      <footer class="footer"></footer>
    </article>
  </section>

  <!-- row 2 -->
  <section class="row">
    <article class="page">
      <header class="pg-head"><span class="pg-head-mark"></span><h1>Subject introduction</h1></header>
      <div class="content">
        <p class="body">This course prepares analysts to find, rate and report weak points across company networks. Learners work through guided labs, short readings and review tasks that build the habits needed for careful, repeatable security testing in real client work.</p>
        <h2 class="sub">Subject recommended</h2>
        <p class="body">Best suited to staff with basic network knowledge who want to move into testing or audit roles within a security team.</p>
        <h2 class="sub">Professional outcomes</h2>
        <table class="tbl-rule">
          <thead><tr><th colspan="2">Work Roles – Table 1</th></tr></thead>
          <tbody>
            <tr><td colspan="2">Work Role Name</td></tr>
            <tr><td colspan="2">Specialty Area</td></tr>
            <tr><td colspan="2">CSF Category</td></tr>
            <tr><td colspan="2">Work Role Description</td></tr>
            <tr><td>Tasks</td><td>This is task 1<br>This is task 2</td></tr>
            <tr><td>Skills</td><td>This is skill 1<br>This is skill 2</td></tr>
            <tr><td>Abilities</td><td>This is ability 1<br>This is ability 2</td></tr>
          </tbody>
        </table>
      </div>
      <footer class="footer"></footer>
    </article>

    <article class="page">
      <header class="pg-head"><span class="pg-head-mark"></span><h1>Training content</h1></header>
      <div class="content">
        <table class="tbl-rule"><thead><tr><th colspan="2">Module 1 – Table 2</th></tr></thead><tbody>
          <tr><td>Name</td><td>Week</td></tr><tr><td colspan="2">Module Description</td></tr><tr><td colspan="2">Acquired Competences</td></tr><tr><td colspan="2">Deliverables</td></tr><tr><td colspan="2">Assessment system</td></tr></tbody></table>
        <table class="tbl-rule"><thead><tr><th colspan="2">Module 2 – Table 2</th></tr></thead><tbody>
          <tr><td>Name</td><td>Week</td></tr><tr><td colspan="2">Module Description</td></tr><tr><td colspan="2">Acquired Competences</td></tr><tr><td colspan="2">Deliverables</td></tr><tr><td colspan="2">Assessment system</td></tr></tbody></table>
        <table class="tbl-rule"><thead><tr><th colspan="2">Module 3 – Table 2</th></tr></thead><tbody>
          <tr><td>Name</td><td>Week</td></tr><tr><td colspan="2">Module Description</td></tr><tr><td colspan="2">Acquired Competences</td></tr><tr><td colspan="2">Deliverables</td></tr><tr><td colspan="2">Assessment system</td></tr></tbody></table>
        <table class="tbl-rule"><thead><tr><th colspan="2">Module 4 – Table 2</th></tr></thead><tbody>
          <tr><td>Name</td><td>Week</td></tr><tr><td colspan="2">Module Description</td></tr><tr><td colspan="2">Acquired Competences</td></tr><tr><td colspan="2">Deliverables</td></tr><tr><td colspan="2">Assessment system</td></tr></tbody></table>
      </div>
      <footer class="footer"></footer>
    </article>

    <article class="page">
      <header class="pg-head"><span class="pg-head-mark"></span><h1>Technical overview</h1></header>
      <div class="content">
        <p class="body">The review covered external hosts, internal servers and user devices. Each target was tested against agreed rules, and every result was checked twice before it was added to this report.</p>
        <table class="tbl-orange">
          <thead><tr><th colspan="2">Table 3</th></tr><tr><th>Sub heading 1</th><th>Sub heading 2</th></tr></thead>
          <tbody><tr><td>Target 1</td><td>Solution 1</td></tr><tr><td>Target 2</td><td>Solution 2</td></tr></tbody>
        </table>
        <h2 class="sub">Severity rating</h2>
        <h3 class="minor">Critical</h3>
        <p class="body">Issues at this level can affect services and should be fixed within the agreed response window.</p>
        <h3 class="minor">High</h3>
        <p class="body">Issues at this level can affect services and should be fixed within the agreed response window.</p>
        <h3 class="minor">Medium</h3>
        <p class="body">Issues at this level can affect services and should be fixed within the agreed response window.</p>
        <h3 class="minor">Low</h3>
        <p class="body">Issues at this level can affect services and should be fixed within the agreed response window.</p>
      </div>
      <footer class="footer"></footer>
    </article>

    <article class="page">
      <header class="pg-head"><span class="pg-head-mark"></span><h1>Technical overview</h1></header>
      <div class="content">
        <h2 class="sub">Summary of findings</h2>
        <p class="body">The table below lists each finding with its rating so the most urgent work can be planned first.</p>
        <table class="tbl-orange">
          <thead><tr><th colspan="2">Table 4</th></tr><tr><th>Finding Name</th><th>Severity</th></tr></thead>
          <tbody>
            <tr><td>Critical Finding Title</td><td><span class="dot c"></span><span class="t-c">Critical</span></td></tr>
            <tr><td>High Finding Title</td><td><span class="dot h"></span><span class="t-h">High</span></td></tr>
            <tr><td>Medium Finding Title</td><td><span class="dot m"></span><span class="t-m">Medium</span></td></tr>
            <tr><td>Low Finding Title</td><td><span class="dot lw"></span><span class="t-l">Low</span></td></tr>
          </tbody>
        </table>
        <h2 class="sub">Detailed observation</h2>
        <h3 class="minor">Critical findings</h3>
        <div class="finding">
          <div class="finding-head"><span>Insecure configurations<br>identified</span><i class="sev c"></i></div>
          <div class="finding-row"><div class="finding-label">Observation</div><div class="finding-body">Several hosts still use default settings and open admin ports. These gaps let an attacker reach sensitive functions without strong checks and should be closed quickly.</div></div>
          <div class="finding-row"><div class="finding-label">Evidence</div><div class="finding-body"><div class="evidence" role="img" aria-label="Screenshot showing the evidence for this finding"></div></div></div>
        </div>
      </div>
      <footer class="footer"></footer>
    </article>
  </section>

  <!-- row 3 -->
  <section class="row">
    <article class="page">
      <header class="pg-head"><span class="pg-head-mark"></span><h1>Technical overview</h1></header>
      <div class="content">
        <div class="finding">
          <div class="finding-head"><span>Insecure configurations<br>identified</span><i class="sev c"></i></div>
          <div class="finding-row"><div class="finding-label">Recommendation</div><div class="finding-body">Apply a hardened baseline to all hosts, disable unused services and limit admin access to approved addresses only.<ul><li>Review settings after each update.</li><li>Log and alert on admin logins.</li></ul></div></div>
          <div class="finding-row"><div class="finding-label">Assets Affected</div><div class="finding-body"><ul><li>127.0.0.1</li><li>127.0.0.2</li><li>127.0.0.3</li></ul></div></div>
        </div>
        <h3 class="minor">High findings</h3>
        <div class="finding">
          <div class="finding-head"><span>Insecure configurations<br>identified</span><i class="sev h"></i></div>
          <div class="finding-row"><div class="finding-label">Observation</div><div class="finding-body">Several hosts still use default settings and open admin ports. These gaps let an attacker reach sensitive functions without strong checks and should be closed quickly.</div></div>
          <div class="finding-row"><div class="finding-label">Evidence</div><div class="finding-body"><div class="evidence" role="img" aria-label="Screenshot showing the evidence for this finding"></div></div></div>
        </div>
      </div>
      <footer class="footer"></footer>
    </article>

    <article class="page">
      <header class="pg-head"><span class="pg-head-mark"></span><h1>Technical overview</h1></header>
      <div class="content">
        <div class="finding">
          <div class="finding-head"><span>Insecure configurations<br>identified</span><i class="sev h"></i></div>
          <div class="finding-row"><div class="finding-label">Recommendation</div><div class="finding-body">Apply a hardened baseline to all hosts, disable unused services and limit admin access to approved addresses only.<ul><li>Review settings after each update.</li><li>Log and alert on admin logins.</li></ul></div></div>
          <div class="finding-row"><div class="finding-label">Assets Affected</div><div class="finding-body"><ul><li>127.0.0.1</li><li>127.0.0.2</li><li>127.0.0.3</li></ul></div></div>
        </div>
        <h3 class="minor">Medium findings</h3>
        <div class="finding">
          <div class="finding-head"><span>Insecure configurations<br>identified</span><i class="sev m"></i></div>
          <div class="finding-row"><div class="finding-label">Observation</div><div class="finding-body">Several hosts still use default settings and open admin ports. These gaps let an attacker reach sensitive functions without strong checks and should be closed quickly.</div></div>
          <div class="finding-row"><div class="finding-label">Evidence</div><div class="finding-body"><div class="evidence" role="img" aria-label="Screenshot showing the evidence for this finding"></div></div></div>
        </div>
      </div>
      <footer class="footer"></footer>
    </article>

    <article class="page">
      <header class="pg-head"><span class="pg-head-mark"></span><h1>Technical overview</h1></header>
      <div class="content">
        <div class="finding">
          <div class="finding-head"><span>Insecure configurations<br>identified</span><i class="sev m"></i></div>
          <div class="finding-row"><div class="finding-label">Recommendation</div><div class="finding-body">Apply a hardened baseline to all hosts, disable unused services and limit admin access to approved addresses only.<ul><li>Review settings after each update.</li><li>Log and alert on admin logins.</li></ul></div></div>
          <div class="finding-row"><div class="finding-label">Assets Affected</div><div class="finding-body"><ul><li>127.0.0.1</li><li>127.0.0.2</li><li>127.0.0.3</li></ul></div></div>
        </div>
        <h3 class="minor">Low findings</h3>
        <div class="finding">
          <div class="finding-head"><span>Insecure configurations<br>identified</span><i class="sev lw"></i></div>
          <div class="finding-row"><div class="finding-label">Observation</div><div class="finding-body">Several hosts still use default settings and open admin ports. These gaps let an attacker reach sensitive functions without strong checks and should be closed quickly.</div></div>
          <div class="finding-row"><div class="finding-label">Evidence</div><div class="finding-body"><div class="evidence" role="img" aria-label="Screenshot showing the evidence for this finding"></div></div></div>
        </div>
      </div>
      <footer class="footer"></footer>
    </article>

    <article class="page">
      <header class="pg-head"><span class="pg-head-mark"></span><h1>Appendix 01</h1></header>
      <div class="content">
        <h2 class="sub">Engagement methodology</h2>
        <p class="body">Testing followed a clear plan: scope agreement, discovery, manual checks, rating and reporting. Each stage was logged, reviewed by a second analyst and shared with the client contact before the next stage began.</p>
      </div>
      <footer class="footer"></footer>
    </article>
  </section>

  <!-- row 4: back covers -->
  <section class="row">
    <article class="page cover-light back">
      <div class="brand"><span class="brand-name">Velorix</span><span class="brand-dot"></span></div>
      <address class="contact" style="font-style:normal">
        <div class="who">Marina Okafor</div>
        000.000.000.000<br>marina@velorix.com<br>www.velorix.com<br>#, Lorem Ipsum, Lorem Ipsum
      </address>
      <div class="cover-date">DD/MM/YYY</div>
    </article>
    <article class="page cover-dark back">
      <div class="brand"><span class="brand-name">Velorix</span><span class="brand-dot"></span></div>
      <address class="contact" style="font-style:normal">
        <div class="who">Marina Okafor</div>
        000.000.000.000<br>marina@velorix.com<br>www.velorix.com<br>#, Lorem Ipsum, Lorem Ipsum
      </address>
      <div class="cover-date">DD/MM/YYY</div>
    </article>
    <article class="page cover-navy back">
      <div class="brand"><span class="brand-name">Velorix</span><span class="brand-dot"></span></div>
      <address class="contact" style="font-style:normal">
        <div class="who">Marina Okafor</div>
        000.000.000.000<br>marina@velorix.com<br>www.velorix.com<br>#, Lorem Ipsum, Lorem Ipsum
      </address>
      <div class="cover-date">DD/MM/YYY</div>
    </article>
  </section>

</main>
</body>
</html>
```